Banner Ad Design Project

My online radio station features DJ sets periodically. The series is called "Deep Orbit" I need a versatile banner ad that I can add the DJ image to an area and then the date and time. I would assume we would agree the area where I can just add a layer via Photoshop with the DJ image and time info as I have more DJs. I will add one of my DJs images. You can crop as necessary. His airplay time is Friday 2pm set and 8pm set.

This is a DANCE radio station, so bright lights, lasers, etc will all be considered.

The banner size is 960X340

Target Market(s)

LGBT between 16-45

Industry/Entity Type

Radio

Requirements
Should not have
• although this is for LGBT, I do not want to see rainbow flags, headphones or other cheesy common themes

```html
<!DOCTYPE html>
<html lang="en">
<head>
<meta charset="utf-8">
<title>Deep Orbit – Banner</title>
<link rel="stylesheet" href="https://fonts.googleapis.com/css2?family=Syncopate:wght@700&family=Poiret+One&display=swap">
<style>
  :root {
    --page: #ffffff;
    --ink: #ffffff;
    --ember-dark: #3a0a0a;
    --ember: #c4260c;
    --flare: #ff6a1a;
    --glow: #ffb36b;
    --night-blue: #1c3f8f;
    --neon-blue: #3f7fd8;
    --haze: rgba(255, 255, 255, 0.35);
  }
  html, body {
    margin: 0;
    padding: 0;
    width: 1200px;
    height: 1000px;
    overflow: hidden;
    background: var(--page);
  }
  .canvas {
    position: relative;
    width: 1200px;
    height: 1000px;
  }
  .banner {
    position: absolute;
    left: 0;
    top: 287px;
    width: 1200px;
    height: 425px;
    overflow: hidden;
  }
  .banner__scene {
    position: absolute;
    inset: 0;
    background:
      linear-gradient(172deg, transparent 38%, rgba(63,127,216,0.75) 46%, rgba(255,255,255,0.35) 49%, rgba(28,63,143,0.8) 53%, transparent 62%),
      linear-gradient(168deg, transparent 66%, rgba(255,106,26,0.8) 74%, rgba(255,179,107,0.6) 78%, transparent 86%),
      linear-gradient(100deg, var(--ember-dark) 0%, var(--ember) 22%, var(--flare) 45%, var(--ember) 68%, var(--ember-dark) 100%);
  }
  .banner__dj-photo {
    position: absolute;
    left: 925px;
    top: 10px;
    width: 275px;
    height: 415px;
    background: linear-gradient(180deg, rgba(90,90,90,0.9) 0%, rgba(200,120,90,0.85) 35%, rgba(70,70,70,0.95) 75%, rgba(30,30,30,0.95) 100%);
  }
  .banner__overlay {
    position: absolute;
    inset: 0;
  }
  .title {
    font-family: "Syncopate", sans-serif;
    font-weight: 700;
    fill: var(--ink);
  }
  .airtime {
    font-family: "Poiret One", sans-serif;
    fill: var(--ink);
  }
</style>
</head>
<body>
<div class="canvas">
  <section class="banner">
    <div class="banner__scene" role="img" aria-label="Night city street with long-exposure red, orange and blue light trails"></div>
    <svg class="banner__overlay" width="1200" height="425" viewBox="0 0 1200 425" aria-hidden="true">
      <polygon points="850,0 1010,0 1200,90 1200,150" fill="var(--haze)"/>
      <polygon points="880,0 1200,160 1200,230" fill="rgba(255,255,255,0.18)"/>
    </svg>
    <div class="banner__dj-photo" role="img" aria-label="Featured DJ portrait in cap and grey t-shirt"></div>
    <svg class="banner__overlay" width="1200" height="425" viewBox="0 0 1200 425">
      <text class="title" x="30" y="205" font-size="118" textLength="680" lengthAdjust="spacingAndGlyphs" transform="rotate(-7.7 30 205)">DEEP ORBIT</text>
      <text class="airtime" x="62" y="330" font-size="42" textLength="535" lengthAdjust="spacingAndGlyphs" transform="rotate(-9.6 62 330)">FRIDAY 2PM SET AND 8PM SET</text>
    </svg>
  </section>
</div>
</body>
</html>
```